Course Graduation Certificate

This project is not for a flyer but instead for the creation of a course graduation certificate. The final certificate needs to include the Marlowe Summit Aviation Academy logo and the text stating as follows:
Certifies that ___________________________ has satisfactorily completed the course of _______________________________ on ________________________________
I would also like to include some type of gold seal of completion as well as a place to sign my name and credentials at the bottom of the certificate
I have included the Marlowe Summit Aviation Academy logo as well as three other certificate examples for you to work from.
Target Market(s)
Students completing a certification course and receiving a certificate
Look and feel

```html
<!DOCTYPE html>
<html lang="en">
<head>
<meta charset="utf-8">
<title>Marlowe Summit Aviation Academy — Course Certificate</title>
<link rel="stylesheet" href="https://fonts.googleapis.com/css2?family=Cormorant+Garamond:ital,wght@0,500;0,600;1,500&family=Open+Sans:wght@400&display=swap">
<style>
  :root {
    --page-bg: #e6e6e6;
    --frame-navy: #00507c;
    --frame-gold: #c29a3f;
    --paper: #ffffff;
    --paper-shadow: #1d2b3a;
    --brand-blue: #1a66b3;
    --ornament-deep: #2a73bf;
    --ornament-pale: #dbe8f5;
    --ink: #111111;
    --rule: #555555;
    --seal-light: #f6d77a;
    --seal-mid: #e0b23e;
    --seal-dark: #b8862a;
  }
  * { margin: 0; padding: 0; box-sizing: border-box; }
  html, body {
    width: 1200px; height: 874px; overflow: hidden;
    background: var(--page-bg);
  }
  .certificate { position: relative; width: 1200px; height: 874px; }

  .frame-outer {
    position: absolute; left: 52px; top: 48px; width: 1078px; height: 752px;
    background: var(--frame-navy);
  }
  .frame-gold {
    position: absolute; left: 71px; top: 62px; width: 1040px; height: 714px;
    background: var(--frame-gold);
  }
  .paper {
    position: absolute; left: 98px; top: 94px; width: 984px; height: 652px;
    background: var(--paper);
    box-shadow: -3px 3px 0 var(--paper-shadow);
  }

  /* Corner ornaments: L-shaped bands hugging the paper corners */
  .ornament {
    position: absolute; width: 182px; height: 188px;
    opacity: .75;
  }
  .ornament--tl {
    left: 130px; top: 120px;
    background: linear-gradient(135deg, var(--ornament-deep) 0%, var(--ornament-pale) 70%);
    clip-path: polygon(0 0, 100% 0, 100% 30px, 34px 30px, 34px 100%, 0 100%);
  }
  .ornament--tr {
    left: 876px; top: 120px;
    background: linear-gradient(225deg, var(--ornament-deep) 0%, var(--ornament-pale) 70%);
    clip-path: polygon(0 0, 100% 0, 100% 100%, calc(100% - 34px) 100%, calc(100% - 34px) 30px, 0 30px);
  }
  .ornament--bl {
    left: 120px; top: 544px;
    background: linear-gradient(45deg, var(--ornament-deep) 0%, var(--ornament-pale) 70%);
    clip-path: polygon(0 0, 34px 0, 34px calc(100% - 30px), 100% calc(100% - 30px), 100% 100%, 0 100%);
  }
  .ornament--br {
    left: 874px; top: 538px;
    background: linear-gradient(315deg, var(--ornament-deep) 0%, var(--ornament-pale) 70%);
    clip-path: polygon(calc(100% - 34px) 0, 100% 0, 100% 100%, 0 100%, 0 calc(100% - 30px), calc(100% - 34px) calc(100% - 30px));
  }

  .serif { font-family: "Cormorant Garamond", "EB Garamond", Georgia, serif; }
  .centered { position: absolute; left: 0; width: 1200px; text-align: center; line-height: 1; }

  .title-main {
    top: 168px; left: -2px; font-size: 62px; font-weight: 500;
    color: var(--brand-blue); letter-spacing: 1px;
  }
  .title-sub {
    top: 244px; left: -8px; font-size: 38px; font-weight: 500;
    color: var(--ink); letter-spacing: .5px;
  }
  .certifies {
    top: 303px; left: 10px; font-size: 22px; font-style: italic; font-weight: 500; color: var(--ink);
  }
  .completed {
    top: 402px; left: -10px; font-family: "Open Sans", Arial, sans-serif;
    font-size: 13px; color: var(--ink);
  }

  .rule { position: absolute; height: 1px; background: var(--rule); }
  .rule--name { left: 252px; top: 370px; width: 678px; }
  .rule--course { left: 250px; top: 457px; width: 676px; }
  .rule--date { left: 462px; top: 506px; width: 236px; }
  .rule--signature { left: 578px; top: 563px; width: 428px; background: var(--ink); }

  .date-on {
    position: absolute; left: 703px; top: 493px;
    font-family: "Open Sans", Arial, sans-serif; font-size: 13px; color: var(--ink);
  }

  .signatory {
    position: absolute; left: 692px; top: 576px; width: 200px; text-align: center;
    font-size: 21px; font-weight: 500; line-height: 1; color: var(--ink);
  }

  .seal { position: absolute; left: 208px; top: 498px; width: 164px; height: 164px; }

  .academy-name {
    position: absolute; left: 428px; top: 628px; width: 266px; text-align: center;
    font-size: 26px; font-weight: 600; line-height: 1.1; color: var(--brand-blue);
  }
</style>
</head>
<body>
<main class="certificate">
  <div class="frame-outer"></div>
  <div class="frame-gold"></div>
  <div class="paper"></div>

  <div class="ornament ornament--tl" role="img" aria-label="Ornate blue filigree corner ornament"></div>
  <div class="ornament ornament--tr" role="img" aria-label="Ornate blue filigree corner ornament"></div>
  <div class="ornament ornament--bl" role="img" aria-label="Ornate blue filigree corner ornament"></div>
  <div class="ornament ornament--br" role="img" aria-label="Ornate blue filigree corner ornament"></div>

  <h1 class="centered serif title-main">MARLOWE SUMMIT</h1>
  <h2 class="centered serif title-sub">AVIATION ACADEMY</h2>
  <p class="centered serif certifies">Certifies that</p>

  <div class="rule rule--name"></div>
  <p class="centered completed">has satisfactorily completed the course of</p>
  <div class="rule rule--course"></div>
  <div class="rule rule--date"></div>
  <span class="date-on">on</span>

  <svg class="seal" viewBox="0 0 164 164" role="img" aria-label="Gold seal of completion">
    <defs>
      <radialGradient id="sealGold" cx="40%" cy="35%" r="70%">
        <stop offset="0%" stop-color="var(--seal-light)"/>
        <stop offset="60%" stop-color="var(--seal-mid)"/>
        <stop offset="100%" stop-color="var(--seal-dark)"/>
      </radialGradient>
    </defs>
    <circle cx="82" cy="82" r="82" fill="url(#sealGold)"/>
    <circle cx="82" cy="82" r="72" fill="none" stroke="var(--seal-dark)" stroke-width="1.5" opacity=".6"/>
    <circle cx="82" cy="82" r="50" fill="none" stroke="var(--seal-dark)" stroke-width="1.5" opacity=".6"/>
  </svg>

  <div class="rule rule--signature"></div>
  <p class="signatory serif">Authorized Signatory</p>

  <p class="academy-name serif">Marlowe Summit<br>Aviation Academy</p>
</main>
</body>
</html>
```